Investment Memorandum Document

IM for Harbourline Lending Fund - is the document that needs work

Make sure it is all done in MS WORD so that i or lawyers can edit some words if required

the IM is NOT final but its 95% of the way there. Maybe a few more pages and wording changes - but that is something i can do i guess or you can easier adjust

Just to typeset and pretty it all up - a few sample finished products have been uploaded for reference.

QOR IM is the one i like - but feel free to show off your skills

put 1.2 to 1.8 all in contrasting row tables

Target Market(s)

Individual and Institutional investors with money

Industry/Entity Type

Investment Banking

Colors

Designer to choose colors to be used in the design.

Requirements
Must have
• clear professional layout and easy on the eye
• https://www.filecrate-example.net/sh/58k3p71zqx4mwtb/BBDrqLwZmUPxTvnQAHMDE42Kb?dl=0
• use the link above for high res images
Nice to have
• pictures and graphics
Should not have
• cartoons

```html
<!DOCTYPE html>
<html lang="en">
<head>
<meta charset="utf-8">
<title>Harbourline Lending Fund – Information Memorandum Contents</title>
<link href="https://fonts.googleapis.com/css2?family=Questrial&display=swap" rel="stylesheet">
<style>
  :root {
    --backdrop: #f1f0ef;
    --paper: #ffffff;
    --ink: #2b2b2b;
    --ink-soft: #4a4a4a;
    --gold: #b98a4e;
    --gold-light: #d8b27a;
    --teal-deep: #0f4f63;
    --teal-bright: #2c8ea3;
    --mark-grey: #ececec;
  }
  * { box-sizing: border-box; margin: 0; padding: 0; }
  html, body {
    width: 1200px;
    height: 814px;
    overflow: hidden;
    background: var(--backdrop);
    font-family: "Questrial", "Century Gothic", sans-serif;
  }
  .page {
    position: absolute;
    left: 332px;
    top: 27px;
    width: 537px;
    height: 760px;
    background: var(--paper);
    box-shadow: 0 6px 24px rgba(0,0,0,0.08);
    overflow: hidden;
  }
  .brand {
    position: absolute;
    left: 50px;
    top: 42px;
    display: flex;
    align-items: center;
    gap: 10px;
  }
  .brand-square {
    width: 18px;
    height: 18px;
    background: var(--gold);
  }
  .brand-name {
    font-size: 20px;
    letter-spacing: 3px;
    color: var(--ink);
  }
  .photo-strip {
    position: absolute;
    left: 0;
    top: 118px;
    width: 96px;
    height: 192px;
    background: linear-gradient(160deg, var(--teal-deep) 0%, var(--teal-bright) 55%, var(--teal-deep) 100%);
  }
  .contents {
    position: absolute;
    left: 150px;
    top: 80px;
    width: 330px;
  }
  .contents-title {
    font-size: 17px;
    font-variant: small-caps;
    letter-spacing: 1px;
    color: var(--gold);
  }
  .contents-rule {
    width: 46px;
    height: 3px;
    margin: 4px 0 8px;
    background: linear-gradient(90deg, var(--gold), var(--gold-light));
  }
  .toc {
    list-style: none;
  }
  .toc-item {
    display: flex;
    font-size: 10.5px;
    line-height: 16.5px;
    text-transform: uppercase;
    color: var(--ink-soft);
  }
  .toc-number {
    width: 34px;
    flex: none;
  }
  .toc-label { flex: 1; }
  .toc-page {
    width: 30px;
    text-align: right;
  }
  .toc-item.is-intro .toc-number { display: none; }
  .brand-mark-faint {
    position: absolute;
    right: 34px;
    bottom: 150px;
    width: 150px;
    height: 150px;
    border: 22px solid var(--mark-grey);
  }
</style>
</head>
<body>
  <main class="page">
    <header class="brand">
      <span class="brand-square"></span>
      <span class="brand-name">HARBOURLINE</span>
    </header>

    <div class="photo-strip" role="img" aria-label="Cropped teal photograph of a harbour waterfront"></div>

    <section class="contents">
      <h1 class="contents-title">Contents</h1>
      <div class="contents-rule"></div>
      <ol class="toc">
        <li class="toc-item is-intro"><span class="toc-label">Message from the Managing Director</span><span class="toc-page">5</span></li>
        <li class="toc-item"><span class="toc-number">1.</span><span class="toc-label">The Fund</span><span class="toc-page">6</span></li>
        <li class="toc-item"><span class="toc-number">2.</span><span class="toc-label">The Loans</span><span class="toc-page">12</span></li>
        <li class="toc-item"><span class="toc-number">3.</span><span class="toc-label">Risks</span><span class="toc-page">17</span></li>
        <li class="toc-item"><span class="toc-number">4.</span><span class="toc-label">Fees and Costs</span><span class="toc-page">20</span></li>
        <li class="toc-item"><span class="toc-number">5.</span><span class="toc-label">Management of the Fund</span><span class="toc-page">22</span></li>
        <li class="toc-item"><span class="toc-number">6.</span><span class="toc-label">Taxation Information</span><span class="toc-page">26</span></li>
        <li class="toc-item"><span class="toc-number">7.</span><span class="toc-label">Additional Information</span><span class="toc-page">31</span></li>
        <li class="toc-item"><span class="toc-number">8.</span><span class="toc-label">Application Process</span><span class="toc-page">34</span></li>
        <li class="toc-item"><span class="toc-number">9.</span><span class="toc-label">Glossary</span><span class="toc-page">36</span></li>
        <li class="toc-item"><span class="toc-number">10.</span><span class="toc-label">Corporate Directory</span><span class="toc-page">38</span></li>
      </ol>
    </section>

    <div class="brand-mark-faint" aria-hidden="true"></div>
  </main>
</body>
</html>
```